Business Card Design for Boutique Agriculture Consulting Practice

Develop a modern Business card design using uploaded logos . Using the color specs 6C344F rgb(108, 52, 79) The fonts are trajan pro and eurostile. The business owner is a woman and should have a hint of femininity. This is what is behind the naming of the company: Rock roads are synonymous with the rural US landscape, where the corn grows and the cattle graze or for Hollow Creek Consulting home. But don’t let the dust get in your eyes, rock roads have edge and are often the only path to a spectacular destination. To navigate them one must know where they are going, have the courage to take a new path and the willingness to adjust their plans to get there.
Target Market(s)
Marketing Professionals
Industry/Entity Type
Agriculture
Contact Information for Business Card
Marisella Duvane
Title: Founder and CEO
Address: 20847 Pellman Lane, Olathe Kansas 66074
Email: md@hollowcreekadvisory.example
Phone: 428.615.2940
Website: www.hollowcreekadvisory.example
Font styles to use
Other font styles liked:
- trajan pro and eurostile
Requirements
Must have
- Please use the correct color specs. Logo color specs are 6C344F rgb(108, 52, 79) The fonts are trajan pro and eurostile. Name, email and phone be the most important information included on the card
Should not have
- additional graphics

```html
<!DOCTYPE html>
<html lang="en">
<head>
<meta charset="utf-8">
<title>Hollow Creek Consulting – Business Card</title>
<link rel="stylesheet" href="https://fonts.googleapis.com/css2?family=Cinzel:wght@400;500&family=Work+Sans:wght@400&display=swap">
<style>
  :root {
    --backdrop: #d9d9d9;
    --card: #1d1d1e;
    --card-edge: #2a2a2b;
    --ink-light: #f2f2f2;
    --ink-soft: #d6d6d6;
    --ink-silver: #a9a9ab;
    --rule: #cfcfcf;
  }
  * { box-sizing: border-box; margin: 0; padding: 0; }
  html, body {
    width: 1200px; height: 900px; overflow: hidden;
    background: var(--backdrop);
  }
  .canvas {
    position: relative; width: 1200px; height: 900px;
  }
  .card {
    position: absolute; left: 240px; width: 720px; height: 412px;
    background: var(--card);
    border: 1px solid var(--card-edge);
    box-shadow: 0 6px 18px rgba(0,0,0,0.25);
  }
  .card--front { top: 30px; }
  .card--back { top: 458px; }

  .front-wordmark {
    position: absolute; inset: 0;
    display: flex; align-items: center; justify-content: center;
    font-family: "Cinzel", serif; font-weight: 500;
    font-size: 44px; letter-spacing: 1px;
    color: var(--ink-silver);
  }

  .back-wordmark {
    position: absolute; left: 40px; top: 0; width: 290px; height: 100%;
    display: flex; align-items: center; justify-content: center;
    text-align: center;
    font-family: "Cinzel", serif; font-weight: 500;
    font-size: 30px; line-height: 1.25;
    color: var(--ink-light);
  }
  .divider {
    position: absolute; left: 352px; top: 82px;
    width: 1px; height: 250px; background: var(--rule);
  }
  .details {
    position: absolute; left: 384px; top: 84px; right: 20px;
    font-family: "Work Sans", sans-serif; color: var(--ink-soft);
  }
  .details__name {
    font-family: "Cinzel", serif; font-weight: 400;
    font-size: 25px; letter-spacing: 0.5px; color: var(--ink-light);
    line-height: 1.1;
  }
  .details__title { font-size: 15px; margin-top: 4px; }
  .details__address { font-size: 15px; line-height: 1.35; margin-top: 14px; }
  .contact-list { list-style: none; margin-top: 14px; }
  .contact-list li {
    display: flex; align-items: center; gap: 9px;
    font-size: 16px; line-height: 1.6;
  }
  .contact-list svg { width: 12px; height: 12px; flex: none; }
</style>
</head>
<body>
<div class="canvas">
  <section class="card card--front">
    <div class="front-wordmark">Hollow Creek Consulting</div>
  </section>

  <section class="card card--back">
    <div class="back-wordmark">Hollow Creek<br>Consulting</div>
    <div class="divider"></div>
    <div class="details">
      <div class="details__name">Marisella Duvane</div>
      <div class="details__title">Founder and CEO</div>
      <div class="details__address">20847 Pellman Lane,<br>Olathe Kansas 66074</div>
      <ul class="contact-list">
        <li>
          <svg viewBox="0 0 12 12" aria-hidden="true"><path d="M2.5 1 L4.5 1 L5.3 3.4 L4 4.4 C4.7 6 6 7.3 7.6 8 L8.6 6.7 L11 7.5 L11 9.5 C11 10.3 10.3 11 9.5 11 C5 11 1 7 1 2.5 C1 1.7 1.7 1 2.5 1 Z" fill="none" stroke="#d6d6d6" stroke-width="1"/></svg>
          428.615.2940
        </li>
        <li>
          <svg viewBox="0 0 12 12" aria-hidden="true"><rect x="1" y="2.5" width="10" height="7" fill="none" stroke="#d6d6d6" stroke-width="1"/><path d="M1 2.5 L6 6.5 L11 2.5" fill="none" stroke="#d6d6d6" stroke-width="1"/></svg>
          md@hollowcreekadvisory.example
        </li>
        <li>
          <svg viewBox="0 0 12 12" aria-hidden="true"><circle cx="6" cy="6" r="5" fill="none" stroke="#d6d6d6" stroke-width="1"/><ellipse cx="6" cy="6" rx="2.2" ry="5" fill="none" stroke="#d6d6d6" stroke-width="0.9"/><path d="M1 6 H11" stroke="#d6d6d6" stroke-width="0.9"/></svg>
          www.hollowcreekadvisory.example
        </li>
      </ul>
    </div>
  </section>
</div>
</body>
</html>
```